Venture Backed Startup Company for SaaS Lead Generation ***Guaranteed Payment and Fast Feedback***

***Guaranteed Payment***
***I Give Fast Feedback***

I need a one-page website design for a startup company. We sell lead generation and appointment setting services to B2B SaaS companies.

Looking for a clean, modern, flat, "Saas-style" design. A simple but trustworthy and authoritative color palette is best. Pictures of actual people are very good to use too

Here are some websites I like and the reasons why:

https://www.plimwerk.com - simple and intuitive design, very clear, strong CTA, explains the process succinctly, and has pics of people/faces\

https://www.tarnoseed.com/ - clean and simple, flat design, strong CTA, easy to understand

https://www.vurmtile.io/ - simple and clean navigation, easy to understand what to do next

https://quillbrashvantor.com/ - strong step by step approach, easy to understand the value of the website, clean and sharp design

https://pebrikloft.com/ - Great color scheme, clean, easy to read, great font

Target Market(s)

startups, entrepeneur, B2B SaaS

Industry/Entity Type

SaaS

Number of Pages Required

1 page

Font styles to use
Sans Serif

Colors

Designer to choose colors to be used in the design.

Requirements
Must have
• Good graphics, a theme, and pictures of people
Nice to have
• Here are other websites like and the reason why
• https://marzentilo.com/ - Great graphics, clean and flat design, pictures of people, modern design
• https://drovelunk.com/ - Clean, pictures of people, easy to read, good contrast
• https://pelkiwarn.co/ -- Good graphics and great font, easy to read, great color scheme
• http://fennicandwest.com/ - clean design

```html
<!DOCTYPE html>
<html lang="en">
<head>
<meta charset="UTF-8">
<title>Lumora Leads — Lead Generation &amp; Appointment Setting</title>
<link rel="stylesheet" href="https://fonts.googleapis.com/css2?family=Montserrat:wght@500;600;700&display=swap">
<style>
  :root {
    --brand-blue: #1a78f2;
    --brand-blue-deep: #0f62e8;
    --brand-blue-light: #3aa6ff;
    --headline-blue: #2a6fd4;
    --nav-blue: #1f5fc4;
    --accent-orange: #ff8a2a;
    --accent-orange-deep: #ff5a1f;
    --tint: #f1f6fd;
    --white: #ffffff;
  }
  * { margin: 0; padding: 0; box-sizing: border-box; }
  html, body { width: 1200px; height: 638px; overflow: hidden; background: var(--white); }
  body { font-family: "Montserrat", sans-serif; position: relative; }

  .backdrop { position: absolute; inset: 0; width: 1200px; height: 638px; }

  .site-header { position: absolute; top: 0; left: 0; width: 1200px; height: 100px; }
  .brand {
    position: absolute; left: 120px; top: 36px;
    display: flex; align-items: center; gap: 12px;
    color: var(--white); font-weight: 600; font-size: 16px; letter-spacing: 0.2px;
  }
  .brand-mark {
    width: 38px; height: 38px; border-radius: 50%;
    border: 5px solid var(--white);
  }
  .main-nav a {
    position: absolute; top: 50px;
    color: var(--nav-blue); font-size: 13.6px; font-weight: 500; text-decoration: none;
  }
  .main-nav a.is-active::after {
    content: ""; position: absolute; left: 0; right: 0; top: 33px;
    height: 3px; background: var(--accent-orange-deep);
  }
  .btn {
    position: absolute; display: flex; align-items: center; justify-content: center;
    height: 43px; border-radius: 22px;
    background: linear-gradient(90deg, var(--accent-orange), var(--accent-orange-deep));
    color: var(--white); font-weight: 600; text-decoration: none;
    box-shadow: 0 10px 18px rgba(255, 110, 40, 0.22);
  }
  .btn-signup { left: 1005px; top: 38px; width: 104px; font-size: 14px; }

  .hero-copy { position: absolute; left: 120px; top: 254px; }
  .hero-title {
    color: var(--headline-blue); font-weight: 700; font-size: 35px; line-height: 48px;
    letter-spacing: -0.2px;
  }
  .btn-learn { left: 120px; top: 442px; width: 144px; font-size: 13px; }
</style>
</head>
<body>
  <svg class="backdrop" viewBox="0 0 1200 638" aria-hidden="true">
    <defs>
      <linearGradient id="corner-blue" x1="0" y1="0" x2="1" y2="1">
        <stop offset="0" stop-color="#2a8cff"/>
        <stop offset="1" stop-color="#0d63ea"/>
      </linearGradient>
    </defs>
    <polygon points="430,0 535,0 275,142 240,128" fill="var(--tint)"/>
    <polygon points="0,0 472,0 215,144 185,144 0,44" fill="url(#corner-blue)"/>
    <polygon points="615,225 675,188 745,220 690,260" fill="var(--tint)"/>
    <polygon points="0,612 30,585 80,612 40,638" fill="var(--tint)"/>
    <polygon points="690,520 780,470 900,530 820,580" fill="var(--tint)"/>
  </svg>

  <svg class="backdrop hero-illustration" viewBox="0 0 1200 638" role="img"
       aria-label="Isometric illustration of a rocket launching from a laptop with charts and clouds">
    <defs>
      <linearGradient id="band-blue" x1="0" y1="0" x2="1" y2="1">
        <stop offset="0" stop-color="var(--brand-blue-light)"/>
        <stop offset="1" stop-color="var(--brand-blue)"/>
      </linearGradient>
    </defs>
    <polygon points="670,404 1000,216 1200,328 1200,638 1064,638" fill="url(#band-blue)"/>
  </svg>

  <header class="site-header">
    <div class="brand"><span class="brand-mark"></span>Lumora Leads</div>
    <nav class="main-nav">
      <a href="#" class="is-active" style="left:468px">About Us</a>
      <a href="#" style="left:576px">Features</a>
      <a href="#" style="left:679px">Services</a>
      <a href="#" style="left:780px">Testimonials</a>
      <a href="#" style="left:910px">Pricing</a>
    </nav>
    <a href="#" class="btn btn-signup">Sign Up</a>
  </header>

  <section class="hero-copy">
    <h1 class="hero-title">Lead Generation &amp;<br>Appointment Setting Services<br>for B2B SaaS Companies</h1>
  </section>
  <a href="#" class="btn btn-learn">Learn More</a>
</body>
</html>
```